Rebuild

Hello,
I got a new logo, and a new business name. Now I need that new identity on a new web page.
Please take a look at my existing site. www.critterfixhub.com
and please build me a new website with my new logo and get it posted at my new domain www.tobymarlowcatching.com
Updates
Please include in the design the Radio marketing tagline "Toby Marlow, Raised and Made for Wildlife Control".
I would like to add that it is usually understood that I will capture and remove problem causing animals. However, what I really need to emphasize is that I fortify homes and other structures to keep the animals out long term. Trapping is a temporary solution. Home fortification such as reinforcing vent screens, sealing holes, and constructing secure barriers is the Permanent solution. Kind of like a home security system for vertebrate pests. You don't really need an alarm system if you have the best locks and steel doors.
Obviously, my website is a multiple page website. Some designs will be good for the home page, and others for secondary pages.
Ultimately, I need a good home page that will attract clients, and then good backup pages to explain the different aspects of my work.
I imagine a home page. Sub pages would include Home Fortifications, Species detail pages, Company history, FAQs, Odd and unusual services, specialties, and where to go for the things I don't do. The text for these pages is something I can write myself. I'm a good writer. Just not a very good visual artist.
I have added the logo in .eps, and I have also added the mirror image logo in both eps and jpg. Let me know if other formats are needed.
I've posted a bunch of photos on my facebook for perusal
http://www.facebook.com/pages/Toby-Marlow-Wildlife-Control/735218064391852
Target Market(s)
Upper to middle income homeowners
Industry/Entity Type
Business
Look and feel
Each slider illustrates characteristics of the customer's brand and the style your logo design should communicate.

```html
<!DOCTYPE html>
<html lang="en">
<head>
<meta charset="utf-8">
<title>Toby Marlow Wildlife Control</title>
<link rel="stylesheet" href="https://fonts.googleapis.com/css2?family=Arimo:ital,wght@0,400;0,700;1,400&display=swap">
<style>
  :root {
    --page-bg: #ffffff;
    --nav-bg: #232323;
    --nav-divider: #0c0c0c;
    --nav-text: #ffffff;
    --accent: #f2b705;
    --heading: #2a3320;
    --body-text: #4a4a4a;
    --strong-text: #222222;
    --tagline-gray: #9a9a9a;
    --dot-gray: #dcdcdc;
    --footer-bg: #222222;
    --footer-text: #8a8a8a;
  }
  * { box-sizing: border-box; margin: 0; padding: 0; }
  html, body {
    width: 1157px; height: 1200px; overflow: hidden;
    background: var(--page-bg);
    font-family: "Arimo", Arial, sans-serif;
  }
  .page { position: relative; width: 1157px; height: 1200px; }

  /* Header */
  .brand {
    position: absolute; left: 133px; top: 52px;
    display: flex; align-items: center; gap: 10px;
  }
  .brand-mark { width: 22px; height: 22px; border-radius: 50%; background: var(--accent); }
  .brand-name { font-size: 28px; font-weight: 700; color: var(--heading); }

  .contact {
    position: absolute; right: 93px; top: 14px; text-align: right;
    color: var(--strong-text);
  }
  .contact-phone {
    display: flex; align-items: center; justify-content: flex-end; gap: 6px;
    font-size: 34px; font-weight: 700; color: #1c2414;
  }
  .contact-phone svg { width: 30px; height: 30px; }
  .contact-address { font-size: 15px; font-weight: 700; line-height: 25px; margin-top: 2px; }

  /* Navigation */
  .main-nav {
    position: absolute; left: 45px; top: 162px; width: 1062px; height: 46px;
    background: var(--nav-bg); display: flex;
  }
  .main-nav a {
    display: flex; align-items: center; justify-content: center;
    height: 100%; color: var(--nav-text); text-decoration: none;
    font-size: 14px; border-right: 1px solid var(--nav-divider);
  }
  .main-nav a:last-child { border-right: none; }
  .main-nav a.is-active { color: var(--accent); }

  /* Slider */
  .hero {
    position: absolute; left: 45px; top: 231px; width: 1062px; height: 439px;
    background: #fff; box-shadow: 0 6px 30px rgba(80, 90, 70, 0.28);
  }
  .hero-text { position: absolute; left: 42px; top: 60px; }
  .hero-name { font-size: 37px; font-style: italic; color: var(--tagline-gray); line-height: 1; }
  .hero-title { font-size: 51px; font-weight: 700; line-height: 1.05; color: var(--tagline-gray); }
  .hero-title span { color: var(--accent); }
  .hero-sub { font-size: 17px; font-style: italic; color: var(--tagline-gray); margin-top: 2px; }
  .hero-photo {
    position: absolute; left: 520px; top: 17px; width: 508px; height: 394px;
    background: radial-gradient(ellipse at 45% 50%, #8f8b84 0%, #bdb9b2 45%, #ffffff 72%);
  }
  .hero-dots { position: absolute; left: 42px; top: 383px; display: flex; gap: 6px; }
  .hero-dots span { width: 23px; height: 23px; border-radius: 50%; background: var(--dot-gray); }
  .hero-dots span.is-current { background: radial-gradient(circle at 40% 30%, #ffe55a, #e0a800 70%); }

  /* Main content */
  .intro { position: absolute; left: 90px; top: 700px; width: 635px; }
  .section-title { font-size: 29px; font-weight: 700; color: var(--heading); margin-left: 3px; }
  .intro-body { margin-top: 30px; font-size: 14px; line-height: 26.5px; color: var(--body-text); letter-spacing: 0.2px; }
  .intro-photo {
    float: left; width: 272px; height: 185px; margin-right: 22px;
    background: linear-gradient(135deg, #6f6a60, #a99a7d 50%, #4d4b48);
  }
  .intro-lead { font-weight: 700; color: var(--strong-text); font-size: 15px; margin-bottom: 10px; line-height: 26px; }
  .intro-body p.plain { padding-left: 3px; }
  .read-more {
    display: flex; align-items: center; justify-content: space-between;
    margin-top: 30px; margin-left: 4px; width: 181px; height: 47px;
    border-radius: 24px; border: 1px solid #c8c8c8;
    background: linear-gradient(#fafafa, #dcdcdc);
    padding: 0 5px 0 20px; font-size: 18px; font-weight: 700; color: #4a4a4a;
    text-decoration: none;
  }
  .read-more svg { width: 36px; height: 36px; }

  .features { position: absolute; left: 788px; top: 697px; width: 300px; }
  .features .section-title { margin-left: 4px; }
  .feature { display: flex; gap: 15px; position: absolute; left: 0; }
  .feature svg { width: 86px; height: 86px; flex: none; }
  .feature h3 { font-size: 15px; font-weight: 700; color: var(--strong-text); margin-top: 4px; line-height: 26px; }
  .feature p { font-size: 14px; color: var(--body-text); line-height: 26px; }

  /* Footer */
  .site-footer {
    position: absolute; left: 45px; top: 1163px; width: 1062px; height: 37px;
    background: var(--footer-bg); color: var(--footer-text);
    font-size: 13px; padding: 10px 0 0 45px;
  }
</style>
</head>
<body>
<div class="page">
  <header>
    <div class="brand">
      <span class="brand-mark"></span>
      <span class="brand-name">Toby Marlow</span>
    </div>
    <div class="contact">
      <div class="contact-phone">
        <svg viewBox="0 0 24 24" aria-hidden="true"><path fill="#1c3a10" d="M6.6 2.5c1-.6 2.1-.2 2.5.7l1.2 2.6c.3.8 0 1.6-.7 2l-1.3.8c-.6 2.5.3 5.3 2.5 7.5l1.3-.7c.7-.4 1.6-.2 2 .5l1.6 2.4c.5.8.3 1.9-.5 2.4l-1.3.8C9 23.6 1.8 12.6 5 3.5z"/></svg>
        <span>(200) 555-0148</span>
      </div>
      <div class="contact-address">3577 Street Name, Suite No<br>City, STATE ZIP</div>
    </div>
  </header>

  <nav class="main-nav">
    <a href="#" class="is-active" style="width:126px">HOME</a>
    <a href="#" style="width:154px">ABOUT US</a>
    <a href="#" style="width:207px">ANIMAL CONTROL</a>
    <a href="#" style="width:218px">WILDLIFE SERVICES</a>
    <a href="#" style="width:183px">TESTIMONIALS</a>
    <a href="#" style="width:174px">CONTACT US</a>
  </nav>

  <section class="hero">
    <div class="hero-text">
      <div class="hero-name">TOBY MARLOW</div>
      <div class="hero-title">RAISED <span>AND MADE</span></div>
      <div class="hero-sub">FOR WILDLIFE CONTROL</div>
    </div>
    <div class="hero-photo" role="img" aria-label="Photo of a raccoon standing on a white background"></div>
    <div class="hero-dots">
      <span></span><span class="is-current"></span><span></span><span></span><span></span>
    </div>
  </section>

  <section class="intro">
    <h2 class="section-title">Aeterno Cibo Nostro Iudico Primis</h2>
    <div class="intro-body">
      <div class="intro-photo" role="img" aria-label="Photo of a wildlife control officer in uniform and hat climbing out of a service truck"></div>
      <p class="intro-lead">Ea prompta conceptam maiestatis eum.<br>Mei illud intellegam suscipiantur an. Iudico</p>
      <p>Cu nec velit postea tincidunt, ei sea electram dissentiet, vis at fugit putent tritani. Ius ea quod accusamus laboramus, sea id facilis probatus forensibus. Eos an quis graece salutatus, mea ex mutat libris quaeque. Platonem splendide</p>
      <p class="plain">Cu nec velit postea tincidunt, ei sea electram dissentiet, vis at fugit putent tritani. Ius ea quod accusamus laboramus, sea id facilis probatus forensibus. Eos an quis graece salutatus, mea ex mutat libris quaeque. Platonem splendide definiebas nam in. Mea persius docendi et, esse</p>
    </div>
    <a href="#" class="read-more">Read more
      <svg viewBox="0 0 36 36" aria-hidden="true">
        <circle cx="18" cy="18" r="16" fill="#e6a800" stroke="#fff" stroke-width="2"/>
        <path d="M10 18h13M18 11l7 7-7 7" fill="none" stroke="#fff" stroke-width="3.5" stroke-linecap="round" stroke-linejoin="round"/>
      </svg>
    </a>
  </section>

  <aside class="features">
    <h2 class="section-title">Aeterno Cibo Nostro</h2>
    <div class="feature" style="top:70px">
      <svg viewBox="0 0 86 86" aria-hidden="true">
        <circle cx="43" cy="43" r="41" fill="#e8e8e8" stroke="#bbb"/>
        <circle cx="43" cy="43" r="34" fill="#1a5fb8"/>
        <circle cx="43" cy="25" r="5" fill="#fff"/>
        <rect x="38" y="34" width="10" height="28" rx="2" fill="#fff"/>
      </svg>
      <div><h3>Ea prompta conceptam</h3><p>Cu nec velit postea tincidunt,<br>ei sea electram dissentiet,</p></div>
    </div>
    <div class="feature" style="top:200px">
      <svg viewBox="0 0 86 86" aria-hidden="true">
        <g fill="#c9c9c9" stroke="#999">
          <path d="M37 4h12l2 12 8 4 10-7 8 8-7 10 4 8 12 2v12l-12 2-4 8 7 10-8 8-10-7-8 4-2 12H37l-2-12-8-4-10 7-8-8 7-10-4-8-12-2V37l12-2 4-8-7-10 8-8 10 7 8-4z"/>
        </g>
        <circle cx="43" cy="43" r="14" fill="#f2f2f2" stroke="#999"/>
      </svg>
      <div><h3>Ea prompta conceptam</h3><p>Cu nec velit postea tincidunt,<br>ei sea electram dissentiet,</p></div>
    </div>
    <div class="feature" style="top:332px">
      <svg viewBox="0 0 86 86" aria-hidden="true">
        <ellipse cx="43" cy="62" rx="40" ry="16" fill="#c4c4c4"/>
        <rect x="10" y="34" width="66" height="28" fill="#d84a10"/>
        <ellipse cx="43" cy="62" rx="33" ry="12" fill="#d84a10"/>
        <ellipse cx="43" cy="34" rx="33" ry="18" fill="#f2672a"/>
      </svg>
      <div><h3>Ea prompta conceptam</h3><p>Cu nec velit postea tincidunt,<br>ei sea electram dissentiet,</p></div>
    </div>
  </aside>

  <footer class="site-footer">Copyright © Toby Marlow Animal Control</footer>
</div>
</body>
</html>
```